Lawn Sign Design

I'm looking for a new lawn sign design to help promote our landscape company. We're trying to position ourselves as a leader in our market, so obviously quality and elegance are important to us.

Phone Number: (555) 214-3098
Website: verdalquix.com
Our tagline: "Your hands are full... Let us help"

Full Service
Weekly Sawn Service
Lanscape Lighting
Spring/Fall Clean Ups
Turf Edging
Snow Removal

I have attached a jpg of our logo to help with design colors. I will provide the vector file upon completion of this project.

Feel free to use your imagination. I know little about content of effective lawn signs, so I'm relying a lot on you, the professionals.

Thanks
Updates

Project Deadline Extended
Reason: Haven't found what I'm looking for.

Industry/Entity Type

Landscape

Requirements
Must have
• Class, elegance, professionalism.
Should not have
• Tacky cartoonish looking desings

```html
<!DOCTYPE html>
<html lang="en">
<head>
<meta charset="utf-8">
<title>Verdalquix Landscaping Lawn Sign</title>
<link href="https://fonts.googleapis.com/css2?family=Cinzel:wght@700&family=Roboto+Slab:wght@600&family=Libre+Baskerville&display=swap" rel="stylesheet">
<style>
  :root {
    --backdrop: #34493a;
    --sign-white: #ffffff;
    --brand-green: #006b35;
    --olive-rule: #a4ad55;
    --art-light: #eef4dc;
    --art-mid: #b9d67a;
  }
  html, body {
    margin: 0;
    width: 1200px;
    height: 1000px;
    overflow: hidden;
    background: var(--backdrop);
  }
  .lawn-sign {
    position: absolute;
    left: 85px;
    top: 113px;
    width: 1029px;
    height: 774px;
    background: var(--sign-white);
  }
  .top-rule {
    position: absolute;
    left: 73px;
    top: 80px;
    width: 872px;
    height: 18px;
    background: var(--olive-rule);
  }
  .brand-mark {
    position: absolute;
    left: 50%;
    top: 62px;
    transform: translateX(-50%);
    display: flex;
    align-items: center;
    gap: 12px;
    padding: 0 22px;
    background: var(--sign-white);
    height: 54px;
  }
  .brand-dot {
    width: 20px;
    height: 20px;
    border-radius: 50%;
    background: var(--olive-rule);
  }
  .brand-name {
    font-family: "Roboto Slab", serif;
    font-weight: 600;
    font-size: 34px;
    color: var(--brand-green);
    letter-spacing: 1px;
    white-space: nowrap;
  }
  .headline {
    position: absolute;
    left: 0;
    top: 0;
    width: 1029px;
    height: 300px;
  }
  .headline text {
    font-family: "Cinzel", serif;
    font-weight: 700;
    font-size: 130px;
    fill: var(--brand-green);
  }
  .home-lawn-art {
    position: absolute;
    left: 203px;
    top: 305px;
    width: 615px;
    height: 195px;
    background: linear-gradient(180deg, var(--art-light) 0%, var(--art-mid) 100%);
  }
  .tagline-band {
    position: absolute;
    left: 0;
    top: 515px;
    width: 100%;
    height: 120px;
    background: var(--brand-green);
    display: flex;
    align-items: center;
    justify-content: center;
  }
  .tagline {
    margin: 0;
    font-family: "Roboto Slab", serif;
    font-weight: 600;
    font-size: 46px;
    color: var(--sign-white);
    white-space: nowrap;
  }
  .contact {
    position: absolute;
    left: 63px;
    right: 60px;
    top: 650px;
    height: 105px;
    display: flex;
    align-items: center;
    justify-content: space-between;
    font-family: "Libre Baskerville", serif;
    color: var(--brand-green);
    white-space: nowrap;
  }
  .phone { font-size: 70px; }
  .website { font-size: 40px; }
</style>
</head>
<body>
  <main class="lawn-sign">
    <div class="top-rule"></div>
    <div class="brand-mark">
      <span class="brand-dot"></span>
      <span class="brand-name">Verdalquix</span>
    </div>
    <svg class="headline" viewBox="0 0 1029 300" aria-label="Landscaping">
      <defs>
        <path id="headline-arc" d="M 60 280 Q 514 200 969 280"/>
      </defs>
      <text text-anchor="middle">
        <textPath href="#headline-arc" startOffset="50%" textLength="880" lengthAdjust="spacing">Landscaping</textPath>
      </text>
    </svg>
    <div class="home-lawn-art" role="img" aria-label="Illustration of a house with trees on rolling green lawn"></div>
    <div class="tagline-band">
      <p class="tagline">"Your hands are full...Let us help."</p>
    </div>
    <div class="contact">
      <span class="phone">555.214.3098</span>
      <span class="website">verdalquix.com</span>
    </div>
  </main>
</body>
</html>
```